integrative health clinic-Medical massage, acupuncture, chiropractic

we like our logo, but are open to new ideas. We need a new card design. We have added chiropractic and acupuncture that we have put under the name of the business. We are an integrative medical clinic

Target Market(s)

General public, athletes

Contact Information for Business Card

Phone 5055583927
Fax 5055583926
Hours Monday-Friday 9-6
Saturday 10-6
The 20% can be smaller on the back

Colors
3176b5
0355a3

Requirements
Must have
• Logo but am open to ideas
Nice to have
• We are an integrated medical clinic but also want to be personable. We want the card fun and inviting

```html
<!DOCTYPE html>
<html lang="en">
<head>
<meta charset="utf-8">
<title>Total Motion Wellness – Business Card</title>
<link href="https://fonts.googleapis.com/css2?family=Open+Sans:wght@400;600;700&family=Roboto+Condensed:wght@700&family=Cormorant+Garamond:ital,wght@1,500&display=swap" rel="stylesheet">
<style>
  :root {
    --bg: #d9d9dc;
    --brand-blue: #263c93;
    --ink: #111111;
    --silver: #a8a6aa;
    --paper: #f7f7f7;
    --paper-shade: #e9e9ea;
    --go-grey: #a9a9ab;
  }
  * { box-sizing: border-box; margin: 0; padding: 0; }
  html, body { width: 1200px; height: 1021px; overflow: hidden; }
  body {
    background: var(--bg);
    font-family: "Open Sans", Arial, sans-serif;
    display: flex; flex-direction: column; align-items: center; justify-content: center; gap: 44px;
  }
  .card {
    position: relative; width: 640px; height: 366px; overflow: hidden;
    box-shadow: 0 6px 18px rgba(0,0,0,.18);
  }

  /* Back side */
  .card--back {
    background: var(--brand-blue); color: #fff;
    display: flex; flex-direction: column; align-items: center; padding-top: 58px;
  }
  .brand-dot { width: 46px; height: 46px; border-radius: 50%; background: #fff; }
  .book-title { margin-top: 12px; font-size: 30px; font-weight: 600; letter-spacing: .5px; }
  .offer { display: flex; align-items: center; gap: 4px; margin-top: 8px; }
  .offer__num { font-size: 36px; font-weight: 700; line-height: 1; }
  .offer__text { font-size: 14px; font-weight: 700; line-height: 1.05; text-transform: uppercase; }
  .booking { display: flex; align-items: center; gap: 8px; margin-top: 12px; }
  .booking__url {
    background: #fff; color: var(--ink); border-radius: 4px; width: 380px; height: 38px;
    display: flex; align-items: center; justify-content: center;
    font-size: 16px; font-weight: 700; box-shadow: inset 0 -2px 0 #ccc;
  }
  .booking__go {
    background: var(--go-grey); color: #fff; width: 72px; height: 36px; border-radius: 3px;
    display: flex; align-items: center; justify-content: center; font-size: 17px; font-weight: 600;
  }
  .insurance { margin-top: 20px; font-size: 16px; }
  .social {
    position: absolute; right: 26px; bottom: 24px; display: flex; align-items: center; gap: 6px;
    font-size: 13px; font-weight: 600;
  }
  .social__square { width: 22px; height: 22px; background: #fff; border-radius: 4px; }

  /* Front side */
  .card--front { background: linear-gradient(160deg, var(--paper) 40%, var(--paper-shade)); }
  .front-wave { position: absolute; left: 0; bottom: 0; }
  .front-header { position: absolute; left: 120px; top: 28px; }
  .brand-name {
    font-family: "Roboto Condensed", "Arial Narrow", sans-serif; font-weight: 700;
    font-size: 54px; color: var(--ink); letter-spacing: -.5px; line-height: 1;
    display: flex; align-items: center; gap: 12px;
  }
  .brand-name__dot { width: 34px; height: 34px; border-radius: 50%; background: var(--brand-blue); }
  .tagline {
    font-family: "Cormorant Garamond", Georgia, serif; font-style: italic; font-weight: 500;
    font-size: 24px; color: var(--ink); margin: 4px 0 0 78px;
  }
  .front-body { position: absolute; top: 140px; left: 0; right: 0; display: flex; }
  .services {
    width: 300px; text-align: right; padding-right: 20px; font-size: 17px; line-height: 1.3; color: var(--ink);
  }
  .services__hours { margin-top: 12px; }
  .divider { width: 2px; height: 140px; background: var(--brand-blue); margin-top: 16px; }
  .contact { padding-left: 22px; font-size: 17px; line-height: 1.3; color: var(--ink); }
  .contact__address { margin-bottom: 14px; }
  .contact__row { display: flex; align-items: center; gap: 6px; }
  .contact__row svg { flex: none; }
</style>
</head>
<body>

<section class="card card--back" aria-label="Card back">
  <div class="brand-dot"></div>
  <h2 class="book-title">BOOK ONLINE</h2>
  <div class="offer">
    <span class="offer__num">20</span>
    <span class="offer__text">% off<br>first visit</span>
  </div>
  <div class="booking">
    <div class="booking__url">www.totalmotionwellness.com</div>
    <div class="booking__go">GO</div>
  </div>
  <p class="insurance">We accept some insurances, Worker’s Comp and Personal Injury.</p>
  <div class="social"><span class="social__square"></span>Circlebook</div>
</section>

<section class="card card--front" aria-label="Card front">
  <svg class="front-wave" width="640" height="366" viewBox="0 0 640 366">
    <path d="M0 218 C 120 278, 330 270, 640 344 L640 366 L0 366 Z" fill="var(--silver)"/>
    <path d="M0 236 C 120 292, 330 286, 640 356 L640 366 L0 366 Z" fill="var(--brand-blue)"/>
  </svg>

  <header class="front-header">
    <h1 class="brand-name"><span class="brand-name__dot"></span>Total Motion Wellness</h1>
    <p class="tagline">Sports Therapy and Wellness Center</p>
  </header>

  <div class="front-body">
    <div class="services">
      <p>Specializing in<br>Medical, Sports Massage<br>Chiropractic and Acupuncture</p>
      <p class="services__hours">Monday-Friday 9am - 6pm<br>Saturday 10am - 6pm</p>
    </div>
    <div class="divider"></div>
    <div class="contact">
      <p class="contact__address">4820 Piñon Ridge Rd, Ste 3<br>Santa Fe, NM 87507</p>
      <p class="contact__row">
        <svg width="16" height="16" viewBox="0 0 24 24"><path fill="var(--brand-blue)" d="M6.6 10.8a15 15 0 0 0 6.6 6.6l2.2-2.2c.3-.3.7-.4 1-.2 1.1.4 2.3.6 3.6.6.6 0 1 .4 1 1V20c0 .6-.4 1-1 1A17 17 0 0 1 3 4c0-.6.4-1 1-1h3.5c.6 0 1 .4 1 1 0 1.3.2 2.5.6 3.6.1.3 0 .7-.2 1z"/></svg>
        505-558-3927</p>
      <p class="contact__row">
        <svg width="16" height="16" viewBox="0 0 24 24"><path fill="var(--brand-blue)" d="M6 2h12v6H6zM3 9h18a1 1 0 0 1 1 1v7h-4v5H6v-5H2v-7a1 1 0 0 1 1-1zm5 8v3h8v-3z"/></svg>
        505-558-3926</p>
      <p class="contact__row">
        <svg width="16" height="14" viewBox="0 0 24 18"><rect x="1" y="1" width="22" height="16" fill="none" stroke="var(--brand-blue)" stroke-width="2"/><path d="M1 1l11 9 11-9M1 17l8-7M23 17l-8-7" fill="none" stroke="var(--brand-blue)" stroke-width="2"/></svg>
        info@totalmotionwellness.com</p>
    </div>
  </div>
</section>

</body>
</html>
```